Boutique Sparkling Blanc de Blancs Wine label

We are looking for a label and neck label for our new Sparkling Chardonnay.
Images uploaded include, bubbles and glitter maybe as a faded background for whole label?
We like Refined, elegant yet simple designs.
Have included our current table chardonnay label as example.

Industry/Entity Type

Boutique

Font styles to use
Decorative
Script

Requirements
Must have
• Name - "Beneath the Lanterns"
• Methode Traditionelle
• Blanc de Blancs
• 2015
• Across the Orchard (Brand)
• Adelaide Hills
Nice to have
• Neutral tones
• Sparkles, Glitter, Bubbles
• Traditional, cursive or vine like fonts
• Have attached fonts we used for previous wine label - might be nice to carry through same/similar fonts to continue our brand?
Should not have
• a lot of colour

```html
<!DOCTYPE html>
<html lang="en">
<head>
<meta charset="utf-8">
<title>Beneath the Lanterns – Sparkling Label Options</title>
<link rel="stylesheet" href="https://fonts.googleapis.com/css2?family=Great+Vibes&family=Poiret+One&family=Cinzel:wght@700&display=swap">
<style>
  :root {
    --canvas: #ffffff;
    --frame-line: #6b6b6b;
    --label-ground: #2a2725;
    --paper-edge: #ffffff;
    --silver: #c9c9cc;
    --silver-soft: #a9a5a2;
    --type-light: #e4e2df;
    --vine-dark: #0d0c0c;
    --vine-grey: #6a6866;
  }
  html, body {
    margin: 0;
    padding: 0;
    width: 1200px;
    height: 1000px;
    overflow: hidden;
    background: var(--canvas);
  }
  .board {
    position: relative;
    width: 1200px;
    height: 1000px;
  }
  .label {
    position: absolute;
    background: var(--paper-edge);
    border: 1px solid var(--frame-line);
    box-shadow: 2px 3px 3px rgba(0,0,0,0.35);
    box-sizing: border-box;
  }
  .label--dark-vines { left: 5px; top: 77px; width: 591px; height: 678px; }
  .label--grey-vines { left: 604px; top: 77px; width: 592px; height: 675px; }
  .label__ground {
    position: absolute;
    background: var(--label-ground);
    overflow: hidden;
  }
  .label--dark-vines .label__ground { left: 5px; top: 5px; right: 3px; bottom: 3px; }
  .label--grey-vines .label__ground { left: 11px; top: 13px; right: 12px; bottom: 11px; }

  .vine {
    position: absolute;
    border-radius: 45%;
  }
  .label--dark-vines .vine { background: radial-gradient(ellipse at center, rgba(13,12,12,0.9), rgba(13,12,12,0.25) 70%, transparent); }
  .label--grey-vines .vine { background: radial-gradient(ellipse at center, rgba(106,104,102,0.55), rgba(106,104,102,0.15) 70%, transparent); }

  .title {
    position: absolute;
    left: 0;
    width: 100%;
    margin: 0;
    font-family: "Great Vibes", cursive;
    font-weight: 400;
    color: var(--silver);
    text-align: center;
    line-height: 1;
  }
  .title__line { position: absolute; white-space: nowrap; }
  .title__line--first { font-size: 96px; }
  .title__line--second { font-size: 112px; }

  .details {
    position: absolute;
    left: 0;
    width: 100%;
    text-align: center;
    font-family: "Poiret One", sans-serif;
  }
  .details p { position: absolute; left: 0; width: 100%; margin: 0; line-height: 1; white-space: nowrap; }
  .label--dark-vines .details { color: var(--silver-soft); }
  .label--grey-vines .details { color: var(--type-light); }
  .style { font-size: 29px; }
  .brand { font-size: 29px; }
  .region { font-size: 23px; }
  .label--grey-vines .region { font-size: 27px; }
  .vintage {
    font-family: "Cinzel", serif;
    font-weight: 700;
    font-size: 34px;
    color: var(--silver);
    letter-spacing: 1px;
  }
</style>
</head>
<body>
<main class="board">

  <section class="label label--dark-vines">
    <div class="label__ground">
      <div class="vine" role="img" aria-label="Black curling vine ornament" style="left:-5px; top:198px; width:155px; height:160px;"></div>
      <div class="vine" role="img" aria-label="Black curling vine ornament" style="left:370px; top:465px; width:230px; height:210px;"></div>
      <div class="vine" role="img" aria-label="Black curling vine ornament" style="left:-5px; top:605px; width:170px; height:80px;"></div>

      <h1 class="title" style="top:0;">
        <span class="title__line title__line--first" style="left:110px; top:40px;">Beneath the</span>
        <span class="title__line title__line--second" style="left:170px; top:170px;">Lanterns</span>
      </h1>

      <div class="details">
        <p class="style" style="top:348px; width:590px; left:0;">Methode Traditionelle</p>
        <p class="style" style="top:390px;">Blanc de Blancs</p>
        <p class="brand" style="top:476px;">Across the Orchard</p>
        <p class="region" style="top:511px;">Adelaide Hills</p>
        <p class="vintage" style="top:590px;">2015</p>
      </div>
    </div>
  </section>

  <section class="label label--grey-vines">
    <div class="label__ground">
      <div class="vine" role="img" aria-label="Grey curling vine ornament" style="left:-5px; top:180px; width:140px; height:140px;"></div>
      <div class="vine" role="img" aria-label="Grey curling vine ornament" style="left:370px; top:465px; width:205px; height:160px;"></div>
      <div class="vine" role="img" aria-label="Grey curling vine ornament" style="left:-5px; top:595px; width:130px; height:60px;"></div>

      <h1 class="title" style="top:0;">
        <span class="title__line title__line--first" style="left:100px; top:20px;">Beneath the</span>
        <span class="title__line title__line--second" style="left:160px; top:150px;">Lanterns</span>
      </h1>

      <div class="details">
        <p class="style" style="top:340px;">Methode Traditionelle</p>
        <p class="style" style="top:377px;">Blanc de Blancs</p>
        <p class="brand" style="top:450px;">Across the Orchard</p>
        <p class="region" style="top:486px;">Adelaide Hills</p>
        <p class="vintage" style="top:567px;">2015</p>
      </div>
    </div>
  </section>

</main>
</body>
</html>
```